Kestrel Photography Business Card

I need a business card designed for a photography business based in Perth, Western Australia called Kestrel Photography.

We specialise in wedding, event photography and portrait photography.

The business card must borrow the style of the attached logo.

The hex codes for the colours in the logo are:
#ED1D85 - Pink
#89C23E - Green
#37282F - Black

The name on the card will be:
Name: Toviran
Phone: 0417395268
Website: www.kestrelphotography.com.au
Facebook: kestrelphotography

I am open and happy to accept creative concepts.

I’d like some space at the back for writing notes and appointment details.

```html
<!DOCTYPE html>
<html lang="en">
<head>
<meta charset="utf-8">
<title>Kestrel Photography – Business Card</title>
<link rel="stylesheet" href="https://fonts.googleapis.com/css2?family=Source+Sans+3:wght@400;600&display=swap">
<style>
  :root {
    --ink: #37282f;
    --card-dark: #37282f;
    --muted-mauve: #9a8b91;
    --pink: #ed1d85;
    --green: #89c23e;
    --paper: #ffffff;
    --label: #000000;
  }
  * { margin: 0; padding: 0; box-sizing: border-box; }
  html, body {
    width: 1200px; height: 900px; overflow: hidden;
    background: var(--paper);
    font-family: "Source Sans 3", "Myriad Pro", Arial, sans-serif;
  }
  .sheet { position: relative; width: 1200px; height: 900px; }

  .dimension, .side-label {
    position: absolute; color: var(--label);
    line-height: 1; white-space: nowrap;
  }
  .dimension { font-size: 22px; font-weight: 400; }
  .dimension--width { left: 594px; top: 42px; transform: translateX(-50%); }
  .dimension--height { left: 850px; top: 225px; }
  .side-label { font-size: 22px; font-weight: 600; left: 248px; }
  .side-label--front { top: 220px; }
  .side-label--back { top: 611px; }

  .card { position: absolute; width: 488px; height: 316px; }
  .card--front { left: 349px; top: 70px; background: var(--card-dark); }
  .card--back {
    left: 351px; top: 473px; background: var(--paper);
    border: 2px solid var(--ink);
  }

  .brand-mark {
    position: absolute; left: 50%; transform: translateX(-50%);
    border-radius: 50%;
  }
  .card--front .brand-mark {
    top: 57px; width: 98px; height: 98px; background: var(--muted-mauve);
  }
  .card--back .brand-mark {
    top: 71px; width: 70px; height: 70px; background: var(--pink);
  }

  .brand-name {
    position: absolute; left: 0; right: 0; text-align: center;
    text-transform: uppercase; font-weight: 400; line-height: 1; white-space: nowrap;
  }
  .card--front .brand-name {
    top: 185px; font-size: 15px; letter-spacing: 11.6px;
    padding-left: 11.6px; color: var(--muted-mauve);
  }
  .card--back .brand-name {
    top: 162px; font-size: 11px; letter-spacing: 8px;
    padding-left: 8px; color: var(--ink);
  }

  .phone {
    position: absolute; right: 32px; top: 44px;
    font-size: 16px; font-weight: 600; color: var(--ink); line-height: 1;
  }
  .contact-links {
    position: absolute; left: 0; right: 0; top: 193px;
    text-align: center; font-size: 16px; font-weight: 600;
    color: var(--ink); line-height: 22px; font-style: normal;
  }
</style>
</head>
<body>
<main class="sheet">
  <span class="dimension dimension--width">85mm</span>
  <span class="dimension dimension--height">55mm</span>
  <span class="side-label side-label--front">Front</span>
  <span class="side-label side-label--back">Back</span>

  <section class="card card--front" aria-label="Card front">
    <span class="brand-mark" aria-hidden="true"></span>
    <p class="brand-name">Kestrel Photography</p>
  </section>

  <section class="card card--back" aria-label="Card back">
    <p class="phone">0417395268</p>
    <span class="brand-mark" aria-hidden="true"></span>
    <p class="brand-name">Kestrel Photography</p>
    <address class="contact-links">
      Website: www.kestrelphotography.com.au<br>
      Facebook: kestrelphotography
    </address>
  </section>
</main>
</body>
</html>
```